Food Safety 1-California workers only

3.25" by 4.5" Black and White Magazine Ad
This ad is to train California workers only.
Workers will be trained on: Food Safety, FSMA (Food Safety Modernization Act), using equipment safety, food processing production skills, worker safety, supervisory skills, communication skills.
"FREE TRAINING", The company does the training or Keystone Learning will provide the training.
Training grants range from $100,000 to $400,000.
Companies must be in business for profit.
Companies must train 200 employees or more.
This program is for California workers only.
Incumbent or new-hires are eligible.

Target Market(s)

California food processors, farms, food packaging, food processors, companies under FSMA, food safety, food production who need to train employees.

Industry/Entity Type

Food Production

Font styles to use
Serif
Sans Serif

Colors

Designer to choose colors to be used in the design.

Requirements
Must have
• This is a 3.25 inch by 4.5 inch magazine ad. It must be black and white. No color.
• The deliverable must be in basic PhotoShop. The ad does not need to include any graphics and be text only if needed. If you have a black and white graphic that will show well.
• Look at www.KLGFoodSafety..com
• Use the text from "MEALBOX-Photoshop-052018" file as your starting point.
Nice to have
• A black and white graphic about food. See www.KLGFoodSafety.com
Should not have
• No color.

```html
<!DOCTYPE html>
<html lang="en">
<head>
<meta charset="utf-8">
<title>Free Training – Food Safety Ad</title>
<link rel="stylesheet" href="https://fonts.googleapis.com/css2?family=Bebas+Neue&family=Lato:ital,wght@0,300;0,400;0,700;0,900;1,300&display=swap">
<style>
  :root {
    --ink: #111111;
    --paper: #f1f2f3;
    --backdrop: #e2e3e4;
    --reverse: #ffffff;
  }
  * { margin: 0; padding: 0; box-sizing: border-box; }
  html, body { width: 1200px; height: 1200px; overflow: hidden; }
  body { background: var(--backdrop); position: relative; font-family: "Lato", sans-serif; color: var(--ink); }

  .ad { position: absolute; left: 210px; top: 27px; width: 780px; height: 1145px; background: var(--paper); }
  .ad > * { position: absolute; }

  .headline { left: 0; width: 780px; top: 72px; text-align: center; font-family: "Bebas Neue", sans-serif; font-weight: 400; font-size: 160px; line-height: 1; letter-spacing: 0; }

  .topics { left: 0; width: 734px; top: 226px; text-align: center; line-height: 1; }
  .topic-main { font-weight: 900; font-size: 60px; letter-spacing: 4px; display: block; margin-bottom: 8px; }
  .topic-act { font-weight: 900; font-size: 40px; display: block; margin-bottom: 10px; }
  .topic-light { font-weight: 300; font-size: 42px; display: block; margin-bottom: 6px; }

  .tagline { left: 63px; top: 475px; width: 640px; height: 105px; background: var(--ink); border-radius: 6px; color: var(--reverse); display: flex; align-items: center; justify-content: center; text-align: center; font-style: italic; font-weight: 300; font-size: 31px; line-height: 1.25; }

  .section-label { font-family: "Bebas Neue", sans-serif; font-weight: 400; font-size: 36px; line-height: 1.15; }
  .qualify-label { left: 67px; top: 668px; }

  .criteria-rail { left: 219px; top: 632px; width: 2px; height: 212px; background: var(--ink); }
  .criteria { left: 214px; top: 621px; list-style: none; font-size: 20px; line-height: 34.3px; }
  .criteria li { position: relative; padding-left: 25px; }
  .criteria li::before { content: ""; position: absolute; left: 3px; top: 15px; width: 6px; height: 6px; border-radius: 50%; background: var(--ink); }

  .contact-label { left: 62px; top: 893px; font-size: 34px; }
  .contact-rule { left: 62px; top: 938px; width: 660px; height: 2px; background: var(--ink); }

  .contact-person { left: 62px; top: 952px; font-size: 22px; line-height: 28.6px; font-style: normal; }
  .contact-name { font-weight: 900; font-size: 26px; display: block; margin-bottom: 1px; }

  .contact-divider { left: 410px; top: 992px; height: 98px; border-left: 2px dotted var(--ink); }

  .contact-links { left: 442px; top: 985px; list-style: none; font-size: 22px; line-height: 28.6px; }
  .contact-links li { display: flex; align-items: center; gap: 8px; }
  .contact-links svg { width: 17px; height: 17px; flex: none; }
</style>
</head>
<body>
  <main class="ad">
    <h1 class="headline">FREE TRAINING</h1>

    <div class="topics">
      <span class="topic-main">FOOD SAFETY</span>
      <span class="topic-act">FSMA</span>
      <span class="topic-light">PRODUCTION SKILLS</span>
      <span class="topic-light">WORKER SAFETY</span>
    </div>

    <p class="tagline">“YOU DO THE TRAINING AND THE STATE OF<br>CALIFORNIA PAYS FOR IT!”</p>

    <h2 class="section-label qualify-label">HOW TO<br>QUALIFY:</h2>
    <div class="criteria-rail"></div>
    <ul class="criteria">
      <li>Train California Workers Only</li>
      <li>Trainees must earn <strong>$11/hour</strong></li>
      <li>Full-time workers only</li>
      <li>Employees must attend at least <strong>8 Hours</strong> of training</li>
      <li>You must train 200 or more employees</li>
      <li>Incumbent or New-Hire workers are eligible</li>
      <li>Seasonal workers are eligible</li>
    </ul>

    <h2 class="section-label contact-label">CONTACT:</h2>
    <div class="contact-rule"></div>

    <address class="contact-person">
      <span class="contact-name">Daniel Harlow</span>
      Keystone Learning Company, Inc.<br>
      2150 Meridian Avenue<br>
      Suite 410<br>
      Fairview, CA 92700
    </address>

    <div class="contact-divider"></div>

    <ul class="contact-links">
      <li>
        <svg viewBox="0 0 20 20" fill="none" stroke="currentColor" stroke-width="1.6"><circle cx="10" cy="10" r="8"/><ellipse cx="10" cy="10" rx="3.5" ry="8"/><path d="M2 10h16M3.5 6h13M3.5 14h13"/></svg>
        www.KLGCAL.com
      </li>
      <li>
        <svg viewBox="0 0 20 20" fill="none" stroke="currentColor" stroke-width="1.6"><circle cx="10" cy="10" r="8"/><ellipse cx="10" cy="10" rx="3.5" ry="8"/><path d="M2 10h16M3.5 6h13M3.5 14h13"/></svg>
        www.KLGFoodSafety.com
      </li>
      <li>
        <svg viewBox="0 0 20 20"><rect x="1" y="4" width="18" height="12" fill="currentColor"/><path d="M1.5 4.5 10 11l8.5-6.5" fill="none" stroke="var(--paper)" stroke-width="1.5"/></svg>
        Dan.Harlow@KLGCAL.com
      </li>
      <li>
        <svg viewBox="0 0 20 20"><rect x="3" y="1" width="14" height="18" rx="3" fill="currentColor"/><path d="M8 5c-1 1-1 3 0 6s3 4 4 4l1.5-1.5-2-2-1 .8c-.8-.5-1.5-1.7-1.7-2.6l.9-.8-1-2.6z" fill="var(--paper)"/></svg>
        (555) 014-7781
      </li>
    </ul>
  </main>
</body>
</html>
```